Zielgruppe
für meinen ambulanten Pflegedienst hätte ich gerne Visitenkarten. #
Für zwei Personen mir jeweils gleicher Geschäftsadresse.
KaLuVo Die flinke Pflegehilfe GmbH
www.Kaluvo.de
Das Logo bitte der Homepage entnehmen.
Entwurf bitte für eine Visitenkarte und Briefpapier
Des weiteren wird ein Design für einen runden Leuchtkasten Durchmesser 90 cm benötigt.
Auf dem Briefpapier ist dass noch Kontonummer und Steuernummer zu ergänzen
Aufgabenstellung
Die Visitenkarte sollte elegant und luxuriös sein.

```html
<!DOCTYPE html>
<html lang="de">
<head>
<meta charset="utf-8">
<title>KaLuVo – Visitenkarte</title>
<link rel="stylesheet" href="https://fonts.googleapis.com/css2?family=Montserrat:wght@300;400;500&display=swap">
<style>
  :root {
    --paper: #ffffff;
    --canvas: #ffffff;
    --brand-green: #5a9441;
    --brand-red: #b01c22;
    --ink: #5a5a5a;
    --ink-white: #ffffff;
    --card-shadow: 0 10px 18px rgba(0,0,0,0.28);
  }
  * { margin: 0; padding: 0; box-sizing: border-box; }
  html, body {
    width: 1200px; height: 2298px; overflow: hidden;
    background: var(--canvas);
    font-family: "Montserrat", sans-serif;
  }
  .canvas { position: relative; width: 1200px; height: 2298px; }

  .card {
    position: absolute; left: 285px; width: 630px; height: 418px;
    box-shadow: var(--card-shadow);
    overflow: hidden;
  }
  .card--front { top: 606px; background: var(--paper); }
  .card--back { top: 1274px; background: var(--brand-green); }

  /* Front */
  .wordmark {
    position: absolute; display: flex; align-items: center; gap: 12px;
    font-weight: 400; letter-spacing: 1px;
  }
  .card--front .wordmark {
    left: 60px; top: 188px; font-size: 34px; color: var(--brand-green);
  }
  .wordmark__square {
    width: 26px; height: 26px; background: var(--brand-red);
  }
  .holder { position: absolute; left: 331px; top: 56px; }
  .holder__name { font-size: 19px; color: var(--brand-green); font-weight: 400; line-height: 24px; }
  .holder__title { font-size: 16px; color: var(--ink); font-weight: 300; line-height: 22px; }

  .contact { position: absolute; left: 331px; list-style: none; }
  .contact--phone { top: 169px; }
  .contact--mail { top: 235px; }
  .contact--address { top: 280px; }
  .contact__row { display: flex; gap: 10px; }
  .contact__icon { width: 16px; height: 16px; margin-top: 3px; flex: none; }
  .contact__text { font-size: 16px; line-height: 22.5px; color: var(--ink); font-weight: 300; }

  .band { position: absolute; bottom: 0; height: 26px; width: 315px; }
  .band--red { left: 0; background: var(--brand-red); }
  .band--green { right: 0; background: var(--brand-green); }

  /* Back */
  .card--back .wordmark {
    left: 0; right: 0; top: 165px; justify-content: center;
    font-size: 56px; color: var(--ink-white); gap: 18px;
  }
  .card--back .wordmark__square {
    width: 40px; height: 40px; background: none; border: 3px solid var(--ink-white);
  }
  .website {
    position: absolute; left: 52px; right: 51px; top: 336px;
    display: flex; align-items: center; justify-content: space-between;
  }
  .website__rule { width: 166px; height: 1px; background: var(--ink-white); }
  .website__url { font-size: 17px; font-weight: 300; color: var(--ink-white); letter-spacing: 0.3px; }
</style>
</head>
<body>
<main class="canvas">

  <section class="card card--front" aria-label="Visitenkarte Vorderseite">
    <div class="wordmark"><span class="wordmark__square"></span><span>KaLuVo</span></div>

    <div class="holder">
      <p class="holder__name">NAME SURNAME</p>
      <p class="holder__title">Job title</p>
    </div>

    <ul class="contact contact--phone">
      <li class="contact__row">
        <svg class="contact__icon" viewBox="0 0 24 24" aria-hidden="true"><path fill="#5a9441" d="M6.6 10.8a15.1 15.1 0 0 0 6.6 6.6l2.2-2.2a1 1 0 0 1 1-.25 11.4 11.4 0 0 0 3.6.57 1 1 0 0 1 1 1V20a1 1 0 0 1-1 1A17 17 0 0 1 3 4a1 1 0 0 1 1-1h3.5a1 1 0 0 1 1 1c0 1.25.2 2.45.57 3.57a1 1 0 0 1-.25 1z"/></svg>
        <p class="contact__text">038871-524160<br>01729460573</p>
      </li>
    </ul>

    <ul class="contact contact--mail">
      <li class="contact__row">
        <svg class="contact__icon" viewBox="0 0 24 24" aria-hidden="true"><path fill="#5a9441" d="M2 5h20v14H2z"/><path fill="none" stroke="#fff" stroke-width="2" d="M3 6l9 7 9-7M3 18l6-6m12 6-6-6"/></svg>
        <p class="contact__text">Brandt@Kaluvo.de</p>
      </li>
    </ul>

    <ul class="contact contact--address">
      <li class="contact__row">
        <svg class="contact__icon" viewBox="0 0 24 24" aria-hidden="true"><path fill="#5a9441" d="M12 2a7 7 0 0 0-7 7c0 5 7 13 7 13s7-8 7-13a7 7 0 0 0-7-7zm0 9.5A2.5 2.5 0 1 1 12 6.5a2.5 2.5 0 0 1 0 5z"/></svg>
        <p class="contact__text">KaLuVo<br>Die flinke Pflegehilfe GmbH<br>Lindenweg 14<br>18273 Feldhausen</p>
      </li>
    </ul>

    <div class="band band--red"></div>
    <div class="band band--green"></div>
  </section>

  <section class="card card--back" aria-label="Visitenkarte Rückseite">
    <div class="wordmark"><span class="wordmark__square"></span><span>KaLuVo</span></div>
    <div class="website">
      <span class="website__rule"></span>
      <span class="website__url">www.kaluvo.de</span>
      <span class="website__rule"></span>
    </div>
  </section>

</main>
</body>
</html>
```